Executive recruiting firm in need of business card design

Executive recruiting firm looking for a sleek, classy and modern business card design; card itself will be square shape, rounded edges and soft touch paper, our colors are dark blues in the navy color scale, silvers and grays. Reference our website for a better idea of our company's feel and goals at Staffbrook.com - our company message is "Employee Engagement Begins at Recruitment" this should be on the card

Industry/Entity Type

Business

```html
<!DOCTYPE html>
<html lang="en">
<head>
<meta charset="utf-8">
<title>Staffbrook Business Card</title>
<link href="https://fonts.googleapis.com/css2?family=Roboto:wght@700&family=Work+Sans:wght@400&display=swap" rel="stylesheet">
<style>
  :root {
    --stage: #2b2b2d;
    --navy: #1b1a54;
    --paper: #ffffff;
    --ink-gray: #8a8a8f;
    --tagline: #c9c9dc;
  }
  * { box-sizing: border-box; margin: 0; padding: 0; }
  html, body { width: 1200px; height: 900px; overflow: hidden; }
  body {
    background: var(--stage);
    font-family: "Work Sans", sans-serif;
    position: relative;
  }
  .card {
    position: absolute;
    left: 320px;
    width: 560px;
    height: 320px;
    border-radius: 18px;
  }
  .card-back { top: 100px; background: var(--navy); }
  .card-front { top: 470px; background: var(--paper); }

  .brand-name {
    position: absolute;
    font-family: "Work Sans", sans-serif;
    font-weight: 400;
    font-size: 30px;
    line-height: 1;
  }
  .card-back .brand-name {
    left: 0; right: 0;
    top: 118px;
    text-align: center;
    color: var(--paper);
  }
  .tagline {
    position: absolute;
    left: 0; right: 0;
    top: 222px;
    text-align: center;
    color: var(--tagline);
    font-size: 14px;
    letter-spacing: 1px;
  }

  .card-front .brand-name {
    right: 40px;
    top: 52px;
    color: var(--navy);
    font-size: 26px;
  }

  .person { position: absolute; left: 44px; top: 112px; }
  .person-name {
    font-family: "Roboto", sans-serif;
    font-weight: 700;
    font-size: 21px;
    color: var(--navy);
  }
  .person-role { font-size: 15px; color: var(--ink-gray); margin-top: 2px; }
  .person-rule { width: 18px; height: 2px; background: var(--navy); margin-top: 14px; }

  .contacts { position: absolute; left: 44px; top: 200px; list-style: none; }
  .contacts li {
    display: flex;
    align-items: center;
    gap: 14px;
    font-size: 14px;
    color: var(--ink-gray);
    height: 22px;
  }
  .contacts svg { width: 13px; height: 13px; flex: none; fill: var(--navy); }

  .address {
    position: absolute;
    right: 40px;
    bottom: 36px;
    font-size: 14px;
    line-height: 1.4;
    color: var(--ink-gray);
    text-align: left;
  }
</style>
</head>
<body>
  <section class="card card-back">
    <p class="brand-name">Staffbrook</p>
    <p class="tagline">Employee Engagement Begins at Recruitment</p>
  </section>

  <section class="card card-front">
    <p class="brand-name">Staffbrook</p>

    <div class="person">
      <p class="person-name">Dana Whitfield</p>
      <p class="person-role">Founder</p>
      <div class="person-rule"></div>
    </div>

    <ul class="contacts">
      <li>
        <svg viewBox="0 0 16 16" aria-hidden="true"><path d="M3.6 1.5l2.3 2.6-1.4 1.7c.9 2 2.4 3.6 4.4 4.6l1.7-1.4 2.6 2.3-1.2 2.2C6.9 13.3 2.7 9.1 1.5 2.7z"/></svg>
        <span>+1.212.555.0142</span>
      </li>
      <li>
        <svg viewBox="0 0 16 16" aria-hidden="true"><path d="M4 1h8v14H4zM5.5 2.5v10h5v-10z"/></svg>
        <span>917-555-0188</span>
      </li>
      <li>
        <svg viewBox="0 0 16 16" aria-hidden="true"><path d="M1 3h14v10H1zM2.5 4.5L8 9l5.5-4.5z"/></svg>
        <span>dwhitfield@staffbrook.com</span>
      </li>
    </ul>

    <p class="address">118 Harlow Street Suite #<br>410 New York NY 10012</p>
  </section>
</body>
</html>
```